Card for invoking rights with police

Our criminal defense law firm is seeking proposals for a design for our card intended for clients to carry with them in their car. Upon being pulled over, they would hand this card to the officer.
Text for the back of the card:
"For Law Enforcement:"
"I will comply with lawful orders but respectfully decline any test or other requests without my attorney. I wish to remain silent, do not consent to searches, and request to speak with my attorney now.
The back of the card should prominently feature the text and the firm logo should be secondary.
Front
Must prominently feature contact info: 503-555-0182. Do not include attorney name, email, phone from the example file. This is intended to be generic for the firm and not tied to an individual lawyer.
Included for design reference: current business card, firm logo.
We intend to use trenvo.com to produce the cards.
Updates
The back of the card should prominently display the text regarding invocation of rights. Please title it "For Law Enforcement".
Target Market(s)
People who have been stopped by police
Contact Information for Business Card
see project description
Look and feel

```html
<!DOCTYPE html>
<html lang="en">
<head>
<meta charset="utf-8">
<title>Harlow Law Firm – Cards</title>
<link href="https://fonts.googleapis.com/css2?family=Open+Sans:wght@400;600&display=swap" rel="stylesheet">
<style>
  :root{
    --stage:#1b1c1e;
    --paper:#f7f8f9;
    --navy:#1f4a6e;
    --navy-deep:#0c2641;
    --navy-mid:#17416a;
    --ink:#6b6e72;
    --muted:#8a8d90;
    --light:#dfe6ee;
    --band:rgba(220,228,236,.55);
  }
  *{margin:0;padding:0;box-sizing:border-box}
  html,body{width:1200px;height:900px;overflow:hidden;background:var(--stage);font-family:"Open Sans",Arial,sans-serif}
  .sheet{width:1200px;height:900px;display:flex;flex-direction:column;align-items:center;justify-content:center;gap:40px}
  .card{position:relative;width:700px;height:400px;border-radius:4px;overflow:hidden;box-shadow:0 10px 30px rgba(0,0,0,.5)}

  /* front */
  .card-front{background:var(--paper);color:var(--ink)}
  .light-band{position:absolute;right:0;top:0;width:300px;height:400px;background:linear-gradient(115deg,transparent 40%,var(--band) 40%,var(--band) 58%,transparent 58%)}
  .brand{position:absolute;left:60px;top:52px;display:flex;align-items:center;gap:14px}
  .brand-square{width:34px;height:34px;background:var(--navy);flex:none}
  .brand-name{font-size:26px;font-weight:400;letter-spacing:4px;color:var(--navy);text-transform:uppercase;white-space:nowrap}
  .address{position:absolute;left:60px;top:128px;font-size:16px;line-height:22px}
  .contacts{position:absolute;left:60px;top:218px;list-style:none}
  .contacts li{display:flex;align-items:center;gap:12px}
  .contact-phone{font-size:26px;font-weight:600;color:var(--navy);line-height:36px}
  .contact-phone svg{width:22px;height:22px}
  .contact-web{font-size:16px;line-height:30px;margin-top:4px}
  .contact-web svg{width:14px;height:14px}
  .contacts svg{fill:var(--navy);flex:none}
  .practice{position:absolute;right:60px;bottom:70px;text-align:right}
  .practice-name{font-size:20px;font-weight:600;color:var(--navy);text-transform:uppercase}
  .practice-role{font-size:17px;color:var(--muted);text-transform:uppercase;letter-spacing:1px}

  /* back */
  .card-back{background:radial-gradient(ellipse at 55% 30%,var(--navy-mid) 0%,var(--navy-deep) 85%);color:var(--light);text-align:center}
  .back-brand{position:absolute;left:0;right:0;top:56px;display:flex;align-items:center;justify-content:center;gap:14px}
  .back-brand .brand-square{width:30px;height:30px;background:var(--light)}
  .back-brand .brand-name{color:var(--light);font-size:24px;letter-spacing:6px}
  .rule{position:absolute;top:118px;height:1px;width:120px;background:rgba(223,230,238,.6)}
  .rule-left{left:210px}.rule-right{right:210px}
  .rights-title{position:absolute;left:0;right:0;top:150px;font-size:24px;font-weight:600;letter-spacing:1px;color:#fff}
  .rights{position:absolute;left:70px;right:70px;top:204px;font-size:18px;line-height:30px;color:var(--light)}
</style>
</head>
<body>
<main class="sheet">
  <section class="card card-front">
    <div class="light-band"></div>
    <div class="brand"><span class="brand-square"></span><span class="brand-name">Harlow Law Firm</span></div>
    <p class="address">1250 Alder Ridge Ave<br>Suite 210<br>Lakemont, WA 98101</p>
    <ul class="contacts">
      <li class="contact-phone"><svg viewBox="0 0 16 16"><path d="M3 1h3l1 4-2 1a9 9 0 0 0 5 5l1-2 4 1v3c0 1-1 2-2 2A13 13 0 0 1 1 3c0-1 1-2 2-2z"/></svg>503-555-0182</li>
      <li class="contact-web"><svg viewBox="0 0 16 16"><circle cx="8" cy="8" r="7"/></svg>www.HarlowLawfirm.com</li>
    </ul>
    <div class="practice">
      <p class="practice-name">Criminal Defense</p>
      <p class="practice-role">Attorneys</p>
    </div>
  </section>

  <section class="card card-back">
    <div class="back-brand"><span class="brand-square"></span><span class="brand-name">Harlow Law Firm</span></div>
    <span class="rule rule-left"></span><span class="rule rule-right"></span>
    <h2 class="rights-title">For Law Enforcement:</h2>
    <p class="rights">I will comply with lawful orders but respectfully decline any test or other requests without my attorney. I wish to remain silent, do not consent to searches, and request to speak with my attorney now.</p>
  </section>
</main>
</body>
</html>
```